Brochure Design Project

WE NEED A BROCHURE!!! - This should be easy and allows you to be creative! Plumtree Orbit creates web and mobile portals for businesses in the health and wellness industry. The websites and mobile apps engage our clients' patients and consumers in health and wellness activities such as managing their conditions or losing weight. We leverage our large platform code-stack to build custom solutions for each client. We really love our website www.plumtreeorbit-example.com. So all we need is for someone to take that branding and create a 2-4 page brochure. The text is not that important as we can change it as needed. Mostly we just need the layout. We'd like to include the Sun Ray Hub colors and the JOURNAL font as included on our website.

Industry/Entity Type

Health

Requirements
Must have
• The 2 PDFs uploaded are 2 attempts that we aren't happy with but can be used as a reference only. Please be creative.

Must have the same branding language as our website www.plumtreeorbit-example.com - so that it looks like the same company.

Must have format/room for images. You can plug in stock photography if you'd like and we can buy or add in custom images later.

The font is JOURNAL for the sun/ray/hub. Other fonts are optional. Colors are:

Me – Green RGB 140, 188, 0
We – Blue RGB 11, 116, 187
Info – Orange RGB 237, 137, 33
Dark Gray – RGB 70, 80, 89
Med Gray – 114, 132, 154
Light Gray – 236, 238, 239

Thank you!

```html
<!DOCTYPE html>
<html lang="en">
<head>
<meta charset="utf-8">
<title>Plumtree Orbit – Brochure inner pages</title>
<link rel="stylesheet" href="https://fonts.googleapis.com/css2?family=Open+Sans:ital,wght@0,400;0,600;0,700;1,600&display=swap">
<style>
  :root{
    --green:#8cbc00;
    --blue:#0b74bb;
    --orange:#ed8921;
    --dark:#465059;
    --med:#72849a;
    --light:#eceeef;
    --paper:#ffffff;
    --canvas:#f2f3f4;
    --nav-slate:#5d8aa0;
  }
  *{box-sizing:border-box;margin:0;padding:0}
  html,body{width:1200px;height:900px;overflow:hidden}
  body{background:var(--canvas);font-family:"Open Sans",Arial,sans-serif;color:var(--dark);position:relative}
  .page{position:absolute;top:48px;width:550px;height:712px;background:var(--paper);overflow:hidden}
  .page--left{left:48px}
  .page--right{left:600px}
  .page__header-slant{position:absolute;top:0;right:0;width:260px;height:95px;background:linear-gradient(110deg,transparent 0 30%,#f4f5f6 30% 60%,transparent 60% 68%,#f7f8f8 68%)}
  .brand{position:absolute;left:25px;top:28px;display:flex;align-items:center;gap:8px;font-size:35px;font-weight:700;letter-spacing:-1px;color:var(--dark)}
  .tagline{position:absolute;right:25px;top:50px;font-size:15px;color:var(--dark)}
  .hero{position:absolute;left:0;top:95px;width:550px;background:var(--light)}
  .page--left .hero{height:240px}
  .page--right .hero{height:255px;background:linear-gradient(180deg,#f4f5f6,#fbfbfb)}
  .hero__photo{position:absolute;border-radius:2px;z-index:1}
  .page--left .hero__photo{left:292px;top:82px;width:258px;height:253px;background:linear-gradient(160deg,#f1efec 0%,#e9e5df 20%,#c9c3bb 55%,#f1f1f1 100%)}
  .page--right .hero__photo{left:270px;top:112px;width:280px;height:238px;background:linear-gradient(150deg,#f6ecd9 0%,#e6d5bd 45%,#f3f3f3 75%,#f4b34a 100%)}
  .headline{position:absolute;left:25px;top:112px;font-size:16px;line-height:23px;font-weight:700;letter-spacing:-0.2px;white-space:nowrap;z-index:2}
  .page--left .headline{color:var(--dark)}
  .page--right .headline{color:var(--orange)}
  .lead{position:absolute;left:25px;font-size:10.4px;line-height:18px;color:var(--dark);z-index:2}
  .page--left .lead{top:193px;width:292px}
  .page--right .lead{top:215px;width:245px}
  .pillars{position:absolute;left:25px;top:347px;width:500px;height:26px;display:flex;z-index:2}
  .pillars span{flex:1;text-align:center;font-size:12.5px;font-weight:600;letter-spacing:2.2px;border-left:1px solid #d6d9dc;line-height:26px;white-space:nowrap}
  .pillars span:first-child{border-left:0;text-align:left}
  .pillars span:last-child{text-align:right}
  .screen{position:absolute;top:382px;width:332px;height:257px;background:#fff;border:1px solid #cfd3d6;overflow:hidden;font-size:5.5px;color:#555}
  .page--left .screen{left:25px}
  .page--right .screen{left:25px;width:330px}
  .screen__chrome{height:9px;background:linear-gradient(#e4e6e8,#cdd0d3);border-bottom:1px solid #b8bcc0}
  .feature{position:absolute;top:382px;width:158px;height:257px;color:#fff;padding:12px 10px 0 10px;box-shadow:2px 2px 3px rgba(0,0,0,.18)}
  .page--left .feature{left:367px;background:var(--green)}
  .page--right .feature{left:365px;background:var(--orange)}
  .feature h3{display:flex;align-items:center;gap:10px;font-size:8px;font-weight:700;margin-bottom:14px}
  .feature h3::before{content:"";width:14px;height:14px;background:#fff;flex:none}
  .feature ul{list-style:none;margin-bottom:16px}
  .feature li{font-size:7.4px;line-height:10.5px;margin-bottom:5px;padding-left:6px;text-indent:-6px}
  .feature li::before{content:"• "}
  .footer{position:absolute;left:0;top:672px;width:550px;height:40px}
  .footer__slant{position:absolute;right:0;top:0;width:310px;height:40px;background:var(--light);clip-path:polygon(18px 0,100% 0,100% 100%,0 100%)}
  .footer__url{position:absolute;left:25px;top:13px;font-size:10.5px;font-weight:700}
  .footer__contact{position:absolute;right:25px;top:13px;font-size:10.5px;display:flex;gap:8px}
  .footer__contact strong{font-weight:700}
  .footer__contact .sep{color:#9aa3ab}
  .footer__contact em{font-weight:600}
  /* portal mock – left */
  .pu-head{height:40px;background:linear-gradient(90deg,var(--green),#78ad00);position:relative;color:#fff}
  .pu-brand{position:absolute;left:8px;top:10px;font-size:15px;font-weight:700}
  .pu-slogan{position:absolute;left:110px;top:16px;font-size:7.5px;font-weight:700}
  .pu-points{position:absolute;right:8px;top:13px;font-size:11px;font-weight:700}
  .pu-nav{display:flex;margin-left:102px;border-bottom:2px solid var(--green)}
  .pu-nav span{flex:1;text-align:center;padding:3px 0;border-left:1px solid #ddd}
  .pu-nav span:first-child{background:var(--green);color:#fff}
  .blk{position:absolute}
  .img-fill{background:linear-gradient(135deg,#d9c3b0,#8a6b58)}
  .btn{background:var(--green);color:#fff;padding:2px 4px;display:inline-block}
  .pu-search{border:1px solid #ccc;height:10px;padding:1px 3px;white-space:nowrap;overflow:hidden}
  .orange-btn{background:#e0662a;color:#fff;padding:2px 5px}
  .title-s{font-size:6.5px;color:#333}
  .link{color:var(--blue)}
  /* portal mock – right */
  .hp-nav{height:20px;background:linear-gradient(var(--nav-slate),#3f6f86);display:flex;color:#fff;font-size:5px;margin:2px 8px 0}
  .hp-nav span{padding:3px 5px;border-right:1px solid rgba(255,255,255,.3);line-height:6px}
  .hp-nav span:first-child{background:#d5dde2;color:#3f6f86}
  .hp-bar{background:var(--orange);color:#fff;padding:2px 4px}
  .hp-h{font-size:7px;color:var(--blue);border-bottom:1px solid #ccc;padding-bottom:1px}
</style>
</head>
<body>

<!-- LEFT PAGE -->
<section class="page page--left">
  <div class="page__header-slant"></div>
  <div class="brand">plumtree orbit</div>
  <div class="tagline">Healthy Customer Portals</div>
  <div class="hero"></div>
  <div class="hero__photo" role="img" aria-label="Photo of a smiling older patient greeting his doctor"></div>
  <h2 class="headline">See what a patient-centric approach<br>can do to drive patient engagement,<br>acquisition, and improved outcomes</h2>
  <p class="lead">Provide your patients with the same care and personalization via online and mobile that you do in your hospitals and clinics. Enable your patients to manage their own health and wellness, connect with others and their care teams, and receive personalized, up-to-date information with calls to action.</p>
  <div class="pillars"><span>FLEXIBLE</span><span>BRANDED</span><span>ENGAGEMENT</span><span>SOLUTIONS</span></div>

  <div class="screen">
    <div class="screen__chrome"></div>
    <div class="pu-head">
      <div class="pu-brand">Plate Up</div>
      <div class="pu-slogan">Shop Smart. Eat Healthy.</div>
      <div class="pu-points">200</div>
    </div>
    <div class="pu-nav"><span>Home</span><span>About Me</span><span>My Planner</span><span>Our Community</span><span>Coupon Gallery</span></div>
    <div class="blk img-fill" style="left:4px;top:64px;width:56px;height:58px" role="img" aria-label="Member profile photo"></div>
    <div class="blk" style="left:4px;top:126px;width:58px;line-height:7px">Start messaging with other community members here</div>
    <div class="blk btn" style="left:4px;top:148px">Activate Messages</div>
    <div class="blk link" style="left:4px;top:160px">My Account</div>
    <div class="blk" style="left:14px;top:180px">Sponsored by:</div>
    <div class="blk" style="left:4px;top:188px;width:50px;height:14px;background:#dfe6ee"></div>
    <div class="blk btn" style="left:4px;top:212px;width:54px;height:20px;text-align:center;padding-top:11px">Invite a Friend</div>
    <div class="blk pu-search" style="left:68px;top:66px;width:90px">Search for food and recipes</div>
    <div class="blk pu-search" style="left:160px;top:66px;width:50px">Recipe Exchange</div>
    <div class="blk orange-btn" style="left:214px;top:66px">Search</div>
    <div class="blk" style="left:68px;top:84px;width:160px;border:1px solid #f0c9b5;background:#fff9f5;height:30px;padding:2px 3px">
      <div style="color:#e0662a;font-size:8px;font-weight:700">Welcome!</div>
      <div style="line-height:6px">There are many ways to get started! Create a list or find a recipe.</div>
    </div>
    <div class="blk" style="left:70px;top:118px">Status Update</div>
    <div class="blk pu-search" style="left:68px;top:126px;width:130px">What's on your mind?</div>
    <div class="blk orange-btn" style="left:202px;top:126px">Share</div>
    <div class="blk title-s" style="left:68px;top:150px">What's New</div>
    <div class="blk img-fill" style="left:68px;top:162px;width:24px;height:18px" role="img" aria-label="Recipe thumbnail"></div>
    <div class="blk" style="left:96px;top:162px"><span class="link" style="font-size:6.5px">on my list</span><br>Prep Time: 35 mins</div>
    <div class="blk" style="left:160px;top:172px">1 of 5 ingredients on hand</div>
    <div class="blk img-fill" style="left:68px;top:188px;width:24px;height:18px" role="img" aria-label="Recipe thumbnail"></div>
    <div class="blk" style="left:96px;top:188px"><span class="link" style="font-size:6.5px">Kneidlach</span><br>Prep Time: 30 mins</div>
    <div class="blk" style="left:160px;top:198px">2 of 5 ingredients on hand</div>
    <div class="blk" style="left:68px;top:210px;width:160px;line-height:6px">Light dumplings made simple with a few pantry staples for a family meal.</div>
    <div class="blk" style="left:246px;top:72px;width:34px;height:34px;border-radius:50%;background:conic-gradient(var(--green) 0 25%,var(--orange) 0 50%,var(--blue) 0 75%,#f2c300 0)" role="img" aria-label="Spin the prize wheel graphic"></div>
    <div class="blk" style="left:284px;top:80px;width:44px;line-height:6px">Spin the Plate Up Wheel</div>
    <div class="blk title-s" style="left:244px;top:130px">Most Popular Recipes</div>
    <div class="blk" style="left:244px;top:142px;line-height:7px"><span class="link">fabis french toasts</span><br>Cuisine: American<br>Prep Time: 40 mins</div>
    <div class="blk" style="left:244px;top:172px;line-height:7px"><span class="link">Noa's Favorite Recipe</span><br>Prep Time: 240 mins</div>
    <div class="blk title-s" style="left:244px;top:208px">Top Rated Lists</div>
    <div class="blk link" style="left:244px;top:220px">third</div>
  </div>

  <aside class="feature">
    <h3>Flexible &amp; Market Ready</h3>
    <ul>
      <li>HIPAA compliant &amp; satisfies meaningful use</li>
      <li>EMR, PHR &amp; HRA agnostic</li>
      <li>Flexible to integrate with devices, biometric tests, databases, ecommerce systems, etc.</li>
    </ul>
    <h3>Up-to-date Technology</h3>
    <ul>
      <li>Built in Corvid's latest CoreStack</li>
      <li>Responsive design and Web 2.0 with ‘smart’ planners, memory, drag and drop and optimization for ease of use</li>
    </ul>
  </aside>

  <footer class="footer">
    <div class="footer__slant"></div>
    <div class="footer__url">www.plumtreeorbit-example.com</div>
    <div class="footer__contact"><span><strong>For a demo</strong> contact</span><span class="sep">|</span><em>info@plumtreeorbit-example.com</em></div>
  </footer>
</section>

<!-- RIGHT PAGE -->
<section class="page page--right">
  <div class="page__header-slant"></div>
  <div class="brand">plumtree orbit</div>
  <div class="tagline">Healthy Customer Portals</div>
  <div class="hero"></div>
  <div class="hero__photo" role="img" aria-label="Photo of a doctor examining a young child beside a laptop"></div>
  <h2 class="headline">See what a patient-centric ap-<br>proach can do to drive patient<br>engagement, acquisition, and<br>improved outcomes</h2>
  <p class="lead">Provide your patients with the same care and personalization via online and mobile that you do in your hospitals and clinics. Enable your patients to manage their own health and wellness, connect with others and their care teams, and receive personalized, up-to-date information with calls to action.</p>

  <div class="screen">
    <div class="screen__chrome"></div>
    <div class="hp-nav"><span>My Home</span><span>Services &amp; Conditions</span><span>Locations &amp; Directions</span><span>Patients &amp; Visitors</span><span>Health Resources</span><span>Job Opportunities</span><span>Contact Us</span></div>
    <div class="blk img-fill" style="left:8px;top:42px;width:20px;height:18px" role="img" aria-label="Member photo"></div>
    <div class="blk" style="left:32px;top:44px"><span style="font-size:7px;color:var(--blue)">Welcome, janahealth</span><br>You have no unread messages</div>
    <div class="blk" style="left:196px;top:42px;width:124px;height:20px;background:linear-gradient(90deg,#3a5d8f,#6d8fc0)" role="img" aria-label="Hospital campaign banner"></div>
    <div class="blk hp-h" style="left:8px;top:74px;width:180px">Daily Spoonful <span style="float:right;font-size:5px;color:#777">Saturday, December 29</span></div>
    <div class="blk" style="left:8px;top:88px;width:180px;line-height:6px"><span class="link">More texting, less sleeping.</span><br>A recent study shows teens who text late at night sleep less and feel tired the next day at school.</div>
    <div class="blk hp-h" style="left:8px;top:116px;width:180px">Updates About My Interests</div>
    <div class="blk hp-bar" style="left:8px;top:130px;width:180px">Back and Spine Care</div>
    <div class="blk img-fill" style="left:8px;top:142px;width:30px;height:44px" role="img" aria-label="Video still of lifting a box"></div>
    <div class="blk" style="left:42px;top:144px;width:146px;line-height:6px"><span class="link">Videos: Proper Lifting</span><br>To protect your back when lifting an object, keep your spine in proper alignment and bend at the knees.</div>
    <div class="blk img-fill" style="left:8px;top:192px;width:30px;height:30px" role="img" aria-label="Patient portrait"></div>
    <div class="blk" style="left:42px;top:194px;width:146px;line-height:6px"><span class="link">Rachel's Story</span><br>Hear how our spine team helped a teacher return to her classroom after surgery.</div>
    <div class="blk hp-h" style="left:200px;top:74px;width:120px">My Health Calendar</div>
    <div class="blk" style="left:200px;top:86px">Saturday, December 29, 2012</div>
    <div class="blk hp-h" style="left:200px;top:102px;width:120px">My Doctors</div>
    <div class="blk img-fill" style="left:200px;top:114px;width:18px;height:22px" role="img" aria-label="Doctor portrait"></div>
    <div class="blk" style="left:222px;top:114px;line-height:6px"><span class="link">Dana R Whitfield</span><br>Family Practice<br>555-0148</div>
    <div class="blk hp-h" style="left:200px;top:158px;width:120px">My Notes</div>
    <div class="blk" style="left:200px;top:170px;line-height:6px">Take aspirin at bedtime<br>Review notes from my visit</div>
    <div class="blk hp-h" style="left:200px;top:194px;width:120px">My Folders</div>
    <div class="blk" style="left:200px;top:206px">Heart Care Trips</div>
  </div>

  <aside class="feature">
    <h3>Flexible &amp; Market Ready</h3>
    <ul>
      <li>HIPAA compliant &amp; satisfies meaningful use</li>
      <li>EMR, PHR &amp; HRA agnostic</li>
      <li>Flexible to integrate with devices, biometric tests, databases, ecommerce systems, etc.</li>
    </ul>
    <h3>Up-to-date Technology</h3>
    <ul>
      <li>Built in Corvid's latest CoreStack</li>
      <li>Responsive design and Web 2.0 with ‘smart’ planners, memory, drag and drop and optimization for ease of use</li>
    </ul>
  </aside>

  <footer class="footer">
    <div class="footer__slant"></div>
    <div class="footer__url">www.plumtreeorbit-example.com</div>
    <div class="footer__contact"><span><strong>For a demo</strong> contact</span><span class="sep">|</span><em>info@plumtreeorbit-example.com</em></div>
  </footer>
</section>

</body>
</html>
```